Rising Stewards Scheme. Brochure to Inform Target Audience.

Rising Steward Scheme:

4 Page Brochure
Aimed at Parents and Children (Age 11-16)
Programme Overview
Specific Focus on Copperleaf Award with Learning Objectives and Enabling Objectives from Content Document
Contact Area Needed
How to Book - Online through the Website
Should encourage people to want to join it or sign up

you can use stock rugby images if needed

Target Market(s)

children between ages 11-16 and parents, gatekeepers (schools, rugby clubs)

Industry/Entity Type

Education

Font styles to use
Serif
Sans Serif

Requirements
Must have
• the programme content, each award continent and Copperleaf Award learning objectives
• Colours should match existing work that has been created
• Get in touch: www.harvestmark-rss.com
• maren@harvestmark-rss.com
Nice to have
• graphics of kids playing rugby if possible from stock images

```html
<!DOCTYPE html>
<html lang="en">
<head>
<meta charset="utf-8">
<title>Rising Stewards Scheme – Brochure</title>
<link href="https://fonts.googleapis.com/css2?family=Oswald:wght@500;600&family=Lato:wght@400;700&display=swap" rel="stylesheet">
<style>
:root{
  --backdrop:#2a2a2a;
  --yellow:#fdc41c;
  --black:#000;
  --white:#fff;
  --copper:#6b4226;
  --ink:#222;
  --photo-hall:linear-gradient(160deg,#3d6aa0 0%,#d9a52b 40%,#4d8a6a 75%,#2c4a6a 100%);
  --photo-grass:linear-gradient(180deg,#c0262f 0%,#7a4a2e 35%,#6f8a4a 60%,#50703a 100%);
  --photo-court:linear-gradient(170deg,#3c7fae 0%,#e0b734 35%,#c8392b 55%,#3f7a5c 80%,#2b4d75 100%);
}
*{margin:0;padding:0;box-sizing:border-box}
html,body{width:1200px;height:1200px;overflow:hidden;background:var(--backdrop)}
body{position:relative;font-family:"Lato",sans-serif}
.page{position:absolute;background:var(--white);overflow:hidden;box-shadow:0 4px 14px rgba(0,0,0,.45)}
.heading{font-family:"Oswald",sans-serif;font-weight:600;text-transform:uppercase;line-height:1}
.photo{position:absolute}

/* cover */
.cover{left:173px;top:25px;width:397px;height:557px;background:var(--black)}
.cover .photo.main{left:0;top:0;width:397px;height:402px;background:var(--photo-hall)}
.cover .photo.strip{left:0;bottom:0;width:397px;height:26px;background:linear-gradient(90deg,#3a5a8a,#6a7fa0)}
.seal{position:absolute;left:123px;top:226px;width:152px;height:152px;border-radius:50%;background:var(--black);border:4px solid var(--yellow);display:flex;flex-direction:column;align-items:center;justify-content:center;text-align:center;color:var(--yellow)}
.seal .brand{font-family:"Lato",sans-serif;font-weight:700;font-size:11px;letter-spacing:.5px;margin-bottom:14px}
.seal .brand::before{content:"";display:block;width:22px;height:22px;border-radius:50%;background:var(--yellow);margin:0 auto 6px}
.seal .title{font-size:16px}
.seal .sub{font-size:7px;letter-spacing:2px;margin-top:3px;border-top:1px solid var(--yellow);padding-top:2px}
.cover .tagline{position:absolute;left:0;top:402px;width:397px;height:77px;background:var(--yellow);display:flex;align-items:center;justify-content:center;font-size:19px;color:var(--black);letter-spacing:-.2px;white-space:nowrap}
.cover .contact{position:absolute;left:0;top:479px;width:397px;height:52px;display:flex;flex-direction:column;align-items:center;justify-content:center;color:var(--white);font-size:11.5px;line-height:1.3}

/* overview */
.overview{left:594px;top:25px;width:390px;height:553px}
.overview .photo{left:0;top:0;width:390px;height:287px;background:var(--photo-grass)}
.ov-box{position:absolute;left:178px;top:54px;width:212px}
.ov-box .yl{background:var(--yellow);height:44px;padding:18px 0 0 9px;font-size:19px}
.ov-box .bk{background:var(--black);color:var(--white);height:41px;padding:7px 0 0 9px;font-size:19px}
.ov-box p{background:var(--yellow);height:67px;padding:11px 9px 0;font-size:5.3px;line-height:1.45;text-align:justify}
.award-icon{position:absolute;left:30px;top:299px;width:72px;height:72px;border-radius:8px;background:linear-gradient(160deg,#f4b520,#7a4a25)}
.award-title{position:absolute;left:113px;top:316px;font-size:24px;color:var(--copper);display:flex;align-items:center;font-weight:500;white-space:nowrap}
.award-title .rule{display:inline-block;width:48px;height:2px;background:var(--copper);margin-left:6px;position:relative;flex:none}
.award-title .rule::after{content:"";position:absolute;right:-4px;top:-3px;width:8px;height:8px;border-radius:50%;background:var(--copper)}
.award-text{position:absolute;left:113px;top:347px;width:255px;font-size:5.5px;line-height:1.4;color:var(--ink);text-align:justify}

/* tables */
.obj-table{position:absolute;background:var(--black);border:1px solid #999}
.obj-table .head{display:flex;height:23px;background:var(--yellow)}
.obj-table .head div{display:flex;align-items:center;justify-content:center;font-size:11px;color:#222}
.obj-table .head div:first-child{border-right:2px solid #7a5a00}
.obj-table .body{display:flex;height:calc(100% - 23px)}
.obj-table .col-obj{border-right:2px solid #7a5a00;display:flex;align-items:center;padding-left:13px}
.objective{background:var(--yellow);font-size:5.6px;color:#222;display:flex;padding:4px 6px;width:140px;line-height:1.3}
.objective b{font-weight:400;width:22px;flex:none}
.col-points{display:flex;flex-direction:column;justify-content:center;padding-left:13px;color:var(--white);font-size:5.6px;line-height:1.45}
.col-points li{list-style:none;display:flex}
.col-points li b{font-weight:400;width:23px;flex:none}
.col-points li span{max-width:110px}

.overview .obj-table{left:23px;top:414px;width:343px;height:114px}
.overview .head div:first-child,.overview .col-obj{width:175px}
.overview .head div:last-child,.overview .col-points{width:168px}

.objectives{left:173px;top:625px;width:388px;height:550px}
.objectives .obj-table{left:24px;width:340px;height:113px}
.objectives .head div:first-child,.objectives .col-obj{width:174px}
.objectives .head div:last-child,.objectives .col-points{width:166px}

/* contact */
.back{left:594px;top:625px;width:391px;height:553px;text-align:center}
.back .photo{left:88px;top:35px;width:227px;height:310px;background:var(--photo-court)}
.back .label{position:absolute;left:0;width:100%;font-size:19px;font-weight:500;color:#111}
.back .line{position:absolute;left:0;width:100%;font-size:11.5px;color:#222}
.signup{position:absolute;left:106px;top:454px;width:173px;height:55px;border:3px solid var(--black);border-radius:7px;background:var(--yellow);padding:4px}
.signup span{display:flex;align-items:center;justify-content:center;gap:8px;width:100%;height:100%;border:3px solid var(--white);border-radius:4px;font-size:23px;color:var(--black)}
</style>
</head>
<body>

<!-- Page 1: cover -->
<section class="page cover">
  <div class="photo main" role="img" aria-label="Photo of young players passing a rugby ball in an indoor sports hall"></div>
  <div class="seal">
    <div class="brand">HARVESTMARK RUGBY</div>
    <div class="heading title">Rising Stewards</div>
    <div class="heading sub">SCHEME</div>
  </div>
  <div class="heading tagline">‘Learn to lead and play the Harvestmark way’</div>
  <div class="contact">
    <div>Web:&nbsp; www.harvestmark-rss.com</div>
    <div>Contact us:&nbsp; maren@harvestmark-rss.com</div>
  </div>
  <div class="photo strip" role="img" aria-label="Continuation of the sports hall photo"></div>
</section>

<!-- Page 2: overview and award -->
<section class="page overview">
  <div class="photo" role="img" aria-label="Photo of a child holding a rugby ball above grass"></div>
  <div class="ov-box">
    <div class="heading yl">Programme</div>
    <div class="heading bk">Overview</div>
    <p>Harvestmark have created a scheme which enables each individual to maximise their learning potential so that you can be the best you can be. We provide a fun and healthy environment which is supported by highly motivated coaches who provide excellent individual care and attention. The scheme is delivered over three Awards: Copperleaf, Silver and Gold.</p>
  </div>
  <div class="award-icon" role="img" aria-label="Award emblem"></div>
  <div class="heading award-title">Copperleaf Award<span class="rule"></span></div>
  <p class="award-text">The Copperleaf Award is focused on the ‘Team’ and is aimed at Children between the ages of 11 and 13. During the Award you will improve your self-confidence and independence whilst having the opportunity to lead and inspire others. We will encourage your natural skills and help you identify any areas that you may wish to develop in the future. Each day we will build your skills through both physical and mental challenges both on and off the pitch. The Award is over delivered over 5 days. Days 1 and 2 are delivered at Northbridge Park and days 3 to 5 are delivered at Elmvale Grounds.</p>
  <div class="obj-table">
    <div class="head"><div>Enabling Objective</div><div>Key Learning Points</div></div>
    <div class="body">
      <div class="col-obj"><div class="objective"><b>1.1</b>Discuss the role of leadership</div></div>
      <ul class="col-points">
        <li><b>1.1.1</b><span>Describe who leaders are and how to become a leader</span></li>
        <li><b>1.1.2</b><span>Identify the challenges a leader may face today</span></li>
        <li><b>1.1.3</b><span>Describe the importance of leadership in a team</span></li>
      </ul>
    </div>
  </div>
</section>

<!-- Page 3: objectives -->
<section class="page objectives">
  <div class="obj-table" style="top:38px">
    <div class="head"><div>Enabling Objective</div><div>Key Learning Points</div></div>
    <div class="body">
      <div class="col-obj"><div class="objective"><b>1.2</b>Describe the skills of a leader</div></div>
      <ul class="col-points">
        <li><b>1.2.1</b><span>Explain how a leader develops themselves and their team</span></li>
        <li><b>1.2.2</b><span>Explain the attributes required to be a successful leader</span></li>
        <li><b>1.2.3</b><span>Describe the most important qualities of a leader</span></li>
      </ul>
    </div>
  </div>
  <div class="obj-table" style="top:159px">
    <div class="head"><div>Enabling Objective</div><div>Key Learning Points</div></div>
    <div class="body">
      <div class="col-obj"><div class="objective"><b>1.3</b>Describe what makes a good team leader</div></div>
      <ul class="col-points">
        <li><b>1.3.1</b><span>Explain the difference between a good and a bad leader</span></li>
        <li><b>1.3.2</b><span>Explain what a team needs from their leader</span></li>
        <li><b>1.3.3</b><span>Discuss how you show your leadership in different areas</span></li>
        <li><b>1.3.4</b><span>Explain how you think you could become a better leader in the future</span></li>
      </ul>
    </div>
  </div>
  <div class="obj-table" style="top:280px">
    <div class="head"><div>Enabling Objective</div><div>Key Learning Points</div></div>
    <div class="body">
      <div class="col-obj"><div class="objective"><b>1.4</b>Describe leadership opportunities</div></div>
      <ul class="col-points">
        <li><b>1.4.1</b><span>Explain what leadership opportunities there are within school</span></li>
        <li><b>1.4.2</b><span>Explain leadership opportunities within the community</span></li>
        <li><b>1.4.3</b><span>Explain leadership opportunities within sport</span></li>
      </ul>
    </div>
  </div>
  <div class="obj-table" style="top:402px">
    <div class="head"><div>Enabling Objective</div><div>Key Learning Points</div></div>
    <div class="body">
      <div class="col-obj"><div class="objective"><b>1.5</b>Describe what leadership skill set you have</div></div>
      <ul class="col-points">
        <li><b>1.5.1</b><span>Explain your potential leadership traits</span></li>
        <li><b>1.5.2</b><span>Decide what attributes you need to develop to improve as a leader</span></li>
        <li><b>1.5.3</b><span>Recognise the different areas for development and how to apply them</span></li>
      </ul>
    </div>
  </div>
</section>

<!-- Page 4: contact and booking -->
<section class="page back">
  <div class="photo" role="img" aria-label="Photo of young players running with a rugby ball in a sports hall"></div>
  <div class="heading label" style="top:364px">Contact us:</div>
  <div class="line" style="top:387px">maren@harvestmark-rss.com</div>
  <div class="heading label" style="top:403px">Book online:</div>
  <div class="line" style="top:424px">www.harvestmark-rss.com</div>
  <div class="signup"><span class="heading">Sign up
    <svg width="20" height="24" viewBox="0 0 20 24" aria-hidden="true"><path d="M2 1 L2 19 L7 14 L11 23 L14 21.5 L10 13 L17 13 Z" fill="#000"/></svg>
  </span></div>
</section>

</body>
</html>
```